FC Blavin - Creation of a AD banner for our yearly event

We are a local soccer club in Switzerland. We're organizing a event that will substitute to our yearly club dinner. We need a banner AD to promote on the social networks this event.
We would like to see design that use one or the 2 colors of the club (blue and red).
This Ad should link to a online shop where we can buy vouchers.

Requirements
Must have
• Logo of the club
Title : Souper de gala quand même
Call to action : Plus d'informations
Side texte : Grande Tombola
Banner size : W300xH250 or W300xH600
Nice to have
• Promotion texte: Soutenez le FC Blavin et les restaurateurs locaux

```html
<!DOCTYPE html>
<html lang="fr">
<head>
<meta charset="utf-8">
<title>FC Blavin – Souper de gala quand même</title>
<link href="https://fonts.googleapis.com/css2?family=Montserrat:wght@500;700&family=Barlow:ital,wght@1,800&family=Fira+Sans:ital,wght@1,600&display=swap" rel="stylesheet">
<style>
  :root {
    --paper-red: #dc1e1b;
    --paper-red-light: #e4302a;
    --paper-red-dark: #c81614;
    --cta-red: #990000;
    --art-red: #cf2a24;
    --white: #ffffff;
    --scrap: #f4f2ef;
  }
  * { margin: 0; padding: 0; box-sizing: border-box; }
  html, body { width: 1200px; height: 1000px; overflow: hidden; }
  .banner {
    position: relative;
    width: 1200px;
    height: 1000px;
    overflow: hidden;
    color: var(--white);
    background:
      radial-gradient(ellipse at 20% 15%, var(--paper-red-light) 0%, transparent 55%),
      radial-gradient(ellipse at 80% 70%, var(--paper-red-light) 0%, transparent 50%),
      linear-gradient(160deg, var(--paper-red) 0%, var(--paper-red-dark) 100%);
  }
  .club-mark {
    position: absolute;
    top: 42px;
    right: 48px;
    display: flex;
    align-items: center;
    gap: 14px;
    font-family: "Montserrat", sans-serif;
    font-weight: 700;
    font-size: 40px;
    letter-spacing: 0.5px;
  }
  .club-mark .dot {
    width: 26px;
    height: 26px;
    border-radius: 50%;
    background: var(--white);
  }
  .side-text {
    position: absolute;
    left: 100px;
    top: 196px;
    font-family: "Montserrat", sans-serif;
    font-weight: 500;
    font-size: 56px;
    letter-spacing: 1px;
  }
  .title {
    position: absolute;
    left: 98px;
    top: 322px;
    font-family: "Barlow", sans-serif;
    font-style: italic;
    font-weight: 800;
    font-size: 119px;
    line-height: 122px;
    text-transform: uppercase;
    word-spacing: 8px;
    white-space: nowrap;
  }
  .cta {
    position: absolute;
    left: 100px;
    top: 663px;
    width: 623px;
    height: 124px;
    background: var(--cta-red);
    display: flex;
    align-items: center;
    justify-content: center;
    font-family: "Montserrat", sans-serif;
    font-weight: 500;
    font-size: 53px;
    color: var(--white);
    text-decoration: none;
  }
  .cta-arrow {
    position: absolute;
    left: 745px;
    top: 684px;
  }
  .player-art {
    position: absolute;
    left: 890px;
    top: 445px;
    width: 285px;
    height: 400px;
    border-radius: 24px;
    background: radial-gradient(ellipse at center, #e4524b 0%, var(--art-red) 70%);
  }
  .promo {
    position: absolute;
    left: 103px;
    top: 872px;
    font-family: "Fira Sans", sans-serif;
    font-style: italic;
    font-weight: 600;
    font-size: 45px;
    white-space: nowrap;
  }
  .paper-scrap {
    position: absolute;
    left: 0;
    bottom: 0;
  }
</style>
</head>
<body>
<main class="banner">
  <div class="club-mark"><span class="dot"></span>FC Blavin</div>

  <p class="side-text">Grande Tombola</p>

  <h1 class="title">Souper de gala<br>quand même</h1>

  <a class="cta" href="#">Plus d'informations</a>

  <svg class="cta-arrow" width="135" height="80" viewBox="0 0 135 80" aria-hidden="true">
    <path d="M128 8 C102 32 68 50 8 56" fill="none" stroke="var(--white)" stroke-width="5" stroke-linecap="round"/>
    <path d="M44 28 L8 56 L50 68" fill="none" stroke="var(--white)" stroke-width="5" stroke-linecap="round" stroke-linejoin="round"/>
  </svg>

  <div class="player-art" role="img" aria-label="Line illustration of a footballer kicking a ball"></div>

  <p class="promo">*Soutenez le FC Blavin et les restaurateurs locaux</p>

  <svg class="paper-scrap" width="190" height="100" viewBox="0 0 190 100" aria-hidden="true">
    <path d="M0 0 L30 10 L62 22 L88 40 L118 58 L150 76 L172 90 L190 100 L0 100 Z" fill="var(--scrap)"/>
  </svg>
</main>
</body>
</html>
```